Silver Fern Counseling business cards

Dana Korvath, LCPC, NCC
(410)555-0187
www.silverferncounseling.example
dana@silverferncounseling.example

Business cards. I would like it on the same background as pictured. Not on a white business card. I have attached the logo that was done by another designer with artflockly. I am open to looking at single-sided and double-sided designs.

Target Market(s)

teenagers and adults

Industry/Entity Type

mental health

Contact Information for Business Card

Dana Korvath, LCPC, NCC (410)555-0187 dana@silverferncounseling.example

Font styles to use
Other font styles liked:
• Cinzel

Colors

Designer to choose colors to be used in the design.

Requirements
Must have
• logo that is attached

```html
<!DOCTYPE html>
<html lang="en">
<head>
<meta charset="utf-8">
<title>Silver Fern Counseling — Business Cards</title>
<link rel="stylesheet" href="https://fonts.googleapis.com/css2?family=Montserrat:wght@600;700&family=Open+Sans:wght@400;600;700&display=swap">
<style>
  :root {
    --page-bg: #2a2c2f;
    --front-top: #3a4b58;
    --front-bottom: #1c252d;
    --back-bg: #1f3a52;
    --wordmark: #b7c6ce;
    --mark-dot: #7fb9b3;
    --text-light: #ffffff;
    --accent: #e07a5f;
  }
  * { margin: 0; padding: 0; box-sizing: border-box; }
  html, body { width: 1200px; height: 874px; overflow: hidden; }
  body {
    background: var(--page-bg);
    position: relative;
    font-family: "Open Sans", Arial, sans-serif;
  }
  .card {
    position: absolute;
    left: 290px;
    width: 620px;
    height: 350px;
    border-radius: 18px;
    box-shadow: 0 14px 30px rgba(0,0,0,0.45);
    overflow: hidden;
  }
  .card--front {
    top: 48px;
    background: linear-gradient(160deg, var(--front-top) 0%, var(--front-bottom) 100%);
    display: flex;
    align-items: center;
    justify-content: center;
  }
  .card--back {
    top: 452px;
    background: var(--back-bg);
  }
  .brand {
    display: flex;
    align-items: center;
    gap: 12px;
    font-family: "Montserrat", sans-serif;
    font-weight: 700;
    color: var(--wordmark);
    letter-spacing: 1px;
    text-transform: uppercase;
  }
  .brand__dot {
    width: 16px; height: 16px;
    border-radius: 50%;
    background: var(--mark-dot);
    flex-shrink: 0;
  }
  .card--front .brand { font-size: 28px; }
  .card--back .brand {
    position: absolute;
    right: 40px;
    top: 130px;
    font-size: 19px;
  }
  .contact {
    position: absolute;
    left: 44px;
    top: 150px;
    color: var(--text-light);
  }
  .contact__name {
    font-weight: 700;
    font-size: 20px;
    letter-spacing: 0.5px;
    margin-bottom: 14px;
    text-transform: uppercase;
  }
  .contact__creds { font-size: 15px; font-weight: 700; }
  .contact__line {
    display: flex;
    align-items: center;
    gap: 10px;
    font-size: 17px;
    line-height: 1.6;
  }
  .contact__icon { width: 13px; height: 13px; flex-shrink: 0; }
</style>
</head>
<body>
  <section class="card card--front">
    <div class="brand"><span class="brand__dot"></span>Silver Fern Counseling</div>
  </section>

  <section class="card card--back">
    <div class="contact">
      <p class="contact__name">Dana Korvath, <span class="contact__creds">LCPC, NCC</span></p>
      <p class="contact__line">
        <svg class="contact__icon" viewBox="0 0 24 24" aria-hidden="true"><path fill="var(--accent)" d="M6.6 10.8a15.1 15.1 0 0 0 6.6 6.6l2.2-2.2c.3-.3.7-.4 1-.2 1.1.4 2.3.6 3.6.6.6 0 1 .4 1 1V20c0 .6-.4 1-1 1A17 17 0 0 1 3 4c0-.6.4-1 1-1h3.5c.6 0 1 .4 1 1 0 1.3.2 2.5.6 3.6.1.3 0 .7-.2 1z"/></svg>
        (410)555-0187
      </p>
      <p class="contact__line">
        <svg class="contact__icon" viewBox="0 0 24 24" aria-hidden="true"><rect x="2" y="5" width="20" height="14" rx="2" fill="var(--accent)"/><path d="M3 6l9 7 9-7" stroke="var(--back-bg)" stroke-width="2" fill="none"/></svg>
        dana@silverferncounseling.example
      </p>
      <p class="contact__line">
        <svg class="contact__icon" viewBox="0 0 24 24" aria-hidden="true"><circle cx="12" cy="12" r="10" fill="var(--accent)"/><path d="M2 12h20M12 2c3 3 3 17 0 20M12 2c-3 3-3 17 0 20" stroke="var(--back-bg)" stroke-width="1.5" fill="none"/></svg>
        www.silverferncounseling.example
      </p>
    </div>
    <div class="brand"><span class="brand__dot"></span>Silver Fern Counseling</div>
  </section>
</body>
</html>
```